Business Card Design For Financial Company

Create a new design for company's business card. The corporate logo is attached in several formats. Our new website design is also attached and we would like the business cards to reflect this.
Card needs to contain the following info:
Name
Job Title
Legal company name - eg Varomel Holdings (Asia) Ltd
Address - eg 517-09 Brellford Plaza,46 Tamsworth Lane, Hong Kong
Direct tel
Main tel
Fax
Email
Website URL
MS word format preferred. Other formats that can be edited on standard PC also OK.
Updates
Please note the the "VAROMEL" logo nameĀ font is "Gill Sans MT" on Windows
Target Market(s)
Instituation Investors
Industry/Entity Type
Business
Look and feel
Each slider illustrates characteristics of the customer's brand and the style your logo design should communicate.

```html
<!DOCTYPE html>
<html lang="en">
<head>
<meta charset="utf-8">
<title>Varomel Holdings – Business Card</title>
<link rel="stylesheet" href="https://fonts.googleapis.com/css2?family=Arimo:wght@400;700&display=swap">
<style>
  :root {
    --stage: #1c1c1e;
    --brand-red: #a81d23;
    --brand-red-deep: #8c151b;
    --brand-red-light: #c42f35;
    --paper-top: #f4f4f4;
    --paper-shade: #dcdcdc;
    --ink: #2a2a2a;
    --band-dark: #111111;
    --band-mid: #2a2a2a;
    --band-light: #d6d6d6;
    --white: #ffffff;
  }
  * { box-sizing: border-box; margin: 0; padding: 0; }
  html, body {
    width: 1200px; height: 984px; overflow: hidden;
    background: var(--stage);
    font-family: "Arimo", Arial, sans-serif;
  }
  .card {
    position: absolute; left: 250px;
    width: 700px; height: 400px;
    overflow: hidden;
    box-shadow: 0 10px 30px rgba(0,0,0,.5);
  }

  /* Front */
  .card-front {
    top: 72px;
    background: linear-gradient(100deg, var(--brand-red-deep), var(--brand-red) 55%, var(--brand-red-light));
  }
  .card-front .brand-name {
    position: absolute; left: 40px; top: 258px;
    color: var(--white); font-size: 62px; font-weight: 400;
    letter-spacing: 16px; line-height: 72px;
  }
  .card-front .base-rule {
    position: absolute; left: 0; right: 0; top: 342px; height: 3px;
    background: var(--white);
  }
  .card-front .base-band {
    position: absolute; left: 0; right: 0; top: 345px; bottom: 0;
    background: linear-gradient(90deg, #1a1a1a, #3a3a3a);
  }

  /* Back */
  .card-back { top: 512px; background: var(--brand-red); }
  .card-back .head {
    position: absolute; left: 0; right: 0; top: 0; height: 150px;
    background: linear-gradient(180deg, var(--paper-top), var(--paper-shade));
  }
  .card-back .head .brand-name {
    position: absolute; right: 60px; top: 92px;
    color: var(--ink); font-size: 32px; font-weight: 400;
    letter-spacing: 8px; line-height: 36px;
  }
  .card-back .name-band {
    position: absolute; left: 0; right: 0; top: 150px; height: 40px;
    background: linear-gradient(90deg, var(--band-dark) 0%, var(--band-mid) 40%, var(--band-light) 100%);
    display: flex; align-items: center; padding-left: 40px; gap: 40px;
  }
  .person-name { color: var(--white); font-size: 24px; font-weight: 700; }
  .job-title { color: var(--white); font-size: 15px; font-weight: 400; }
  .card-back .body {
    position: absolute; left: 0; right: 0; top: 190px; bottom: 0;
    background: linear-gradient(180deg, var(--brand-red), var(--brand-red-deep));
  }
  .company {
    position: absolute; left: 40px; top: 28px;
    color: var(--white); font-size: 17px; line-height: 23px; font-style: normal;
  }
  .company .legal-name { font-weight: 700; }
  .contacts {
    position: absolute; left: 370px; top: 48px;
    display: grid; grid-template-columns: 90px auto; row-gap: 4px;
    color: var(--white); font-size: 17px; line-height: 23px;
  }
  .contacts dt { font-weight: 700; }
  .contacts dd { font-weight: 400; }
</style>
</head>
<body>

<section class="card card-front" aria-label="Card front">
  <div class="brand-name">VAROMEL</div>
  <div class="base-rule"></div>
  <div class="base-band"></div>
</section>

<section class="card card-back" aria-label="Card back">
  <div class="head">
    <span class="brand-name">VAROMEL</span>
  </div>
  <div class="name-band">
    <span class="person-name">Daniel Marsh</span>
    <span class="job-title">| Job Title</span>
  </div>
  <div class="body">
    <address class="company">
      <div class="legal-name">Varomel Holdings (Asia) Ltd</div>
      <div>517-09 Brellford Plaza</div>
      <div>46 Tamsworth Lane</div>
      <div>Hong Kong</div>
    </address>
    <dl class="contacts">
      <dt>Direct tel</dt><dd>: +00 123 456 789</dd>
      <dt>Main tel</dt><dd>: +00 123 456 789</dd>
      <dt>Fax</dt><dd>: +00 123 456 789</dd>
      <dt>Email</dt><dd>: office@varomel-mail.com</dd>
      <dt>Web</dt><dd>: www.varomel-holdings.com</dd>
    </dl>
  </div>
</section>

</body>
</html>
```